New Business Card Design Project VORASTI-Italy

we are VORASTI-Italy
our company in the market for 3 years we are luxury cosmetic company and its about time for a facelift :)
i will like to have elegant luxurious and unique business card
that will give the person that get it a unique, luxurious and elegant impression
I'm VERY OPEN FOR NEW IDEAS , even duo i add a few files of things that i see on line and i like them

i add my logo as well
my website is VORASTI.COM
(if you would like to see the main style that we have)

Target Market(s)

adult that have money :)

Industry/Entity Type

Business

Contact Information for Business Card

Name - Paul Vorasti
Position - CEO and CO Founder
address - 4817 E Larkdale
telephone - 555-384-1962
email - paul@vorasti.com
fax - 555-384-1962
website - VORASTI.COM

Colors
000000
959595
fbee3e
ffffff

Requirements
Must have
• big logo in GOLD color
• elegant look
• impressive
Nice to have
• not must but maybe classy pattern background
• not must but maybe emblem
• maybe clear plastic business card
Should not have
• colors
• images

```html
<!DOCTYPE html>
<html lang="en">
<head>
<meta charset="utf-8">
<title>VORASTI Italy – Business Card</title>
<link rel="stylesheet" href="https://fonts.googleapis.com/css2?family=Cinzel:wght@400;600&display=swap">
<style>
  :root {
    --bg: #2a2a2a;
    --card-black: #050505;
    --gold: #d9b443;
    --gold-light: #f3dc7a;
    --gold-deep: #b08a22;
    --ink: #111111;
  }
  * { margin: 0; padding: 0; box-sizing: border-box; }
  html, body { width: 1200px; height: 800px; overflow: hidden; }
  body {
    background: var(--bg);
    font-family: "Cinzel", "Times New Roman", serif;
    display: flex;
    align-items: center;
    justify-content: center;
    gap: 70px;
  }
  .card {
    position: relative;
    width: 500px;
    height: 286px;
    background: var(--card-black);
    overflow: hidden;
  }
  .gold-foil {
    background: linear-gradient(120deg, var(--gold-deep) 0%, var(--gold-light) 35%, var(--gold) 60%, var(--gold-light) 85%, var(--gold-deep) 100%);
  }
  .wordmark {
    position: absolute;
    display: flex;
    flex-direction: column;
    align-items: center;
    color: var(--gold);
    font-weight: 600;
  }
  .wordmark__circle {
    width: 62px;
    height: 62px;
    border-radius: 50%;
    border: 2px solid var(--gold);
    margin-bottom: 10px;
  }
  .wordmark__name {
    font-size: 38px;
    letter-spacing: 2px;
    line-height: 1;
  }
  .wordmark__rule {
    width: 170px;
    height: 2px;
    background: var(--gold);
    margin: 6px 0 4px;
  }
  .wordmark__country {
    font-size: 11px;
    letter-spacing: 2px;
  }

  /* Front */
  .card--front .wordmark { left: 0; right: 0; top: 40px; }
  .card--front .web-band {
    position: absolute;
    left: 0; right: 0; bottom: 34px;
    height: 38px;
    display: flex;
    align-items: center;
    justify-content: center;
    color: var(--ink);
    font-size: 15px;
    letter-spacing: 6px;
  }

  /* Back */
  .card--back .brand-side {
    position: absolute;
    left: 0; top: 0; bottom: 0;
    width: 250px;
  }
  .card--back .wordmark { left: 0; right: 0; top: 58px; }
  .card--back .web-link {
    position: absolute;
    left: 0; right: 0; bottom: 40px;
    text-align: center;
    color: var(--gold);
    font-size: 12px;
    letter-spacing: 3px;
  }
  .card--back .contact-side {
    position: absolute;
    right: 0; top: 0; bottom: 0;
    width: 250px;
    color: var(--ink);
    padding: 70px 0 0 24px;
  }
  .person__name { font-size: 19px; font-weight: 600; letter-spacing: 1px; }
  .person__title { font-size: 10px; letter-spacing: 1px; margin-top: 2px; }
  .contact-list { list-style: none; margin-top: 30px; }
  .contact-list li {
    display: flex;
    align-items: center;
    gap: 8px;
    font-size: 12px;
    height: 19px;
  }
  .contact-list svg { width: 13px; height: 13px; flex: none; }
</style>
</head>
<body>

  <section class="card card--front" aria-label="Card front">
    <div class="wordmark">
      <div class="wordmark__circle"></div>
      <div class="wordmark__name">VORASTI</div>
      <div class="wordmark__rule"></div>
      <div class="wordmark__country">ITALY</div>
    </div>
    <div class="web-band gold-foil">WWW.VORASTI.COM</div>
  </section>

  <section class="card card--back" aria-label="Card back">
    <div class="brand-side">
      <div class="wordmark">
        <div class="wordmark__circle"></div>
        <div class="wordmark__name">VORASTI</div>
        <div class="wordmark__rule"></div>
        <div class="wordmark__country">ITALY</div>
      </div>
      <div class="web-link">WWW.VORASTI.COM</div>
    </div>
    <div class="contact-side gold-foil">
      <div class="person__name">PAUL VORASTI</div>
      <div class="person__title">CEO AND CO FOUNDER</div>
      <ul class="contact-list">
        <li>
          <svg viewBox="0 0 13 13"><rect width="13" height="13" fill="#111"/><path d="M6.5 2.5a2.5 2.5 0 0 1 2.5 2.5c0 2-2.5 5-2.5 5S4 7 4 5a2.5 2.5 0 0 1 2.5-2.5z" fill="#d9b443"/></svg>
          4817 E Larkdale
        </li>
        <li>
          <svg viewBox="0 0 13 13"><rect width="13" height="13" fill="#111"/><path d="M3.5 3h2l.8 2-1.2.8a5 5 0 0 0 2.1 2.1l.8-1.2 2 .8v2a1 1 0 0 1-1 1A6.5 6.5 0 0 1 2.5 4a1 1 0 0 1 1-1z" fill="#d9b443"/></svg>
          555-384-1962
        </li>
        <li>
          <svg viewBox="0 0 13 13"><rect width="13" height="13" fill="#111"/><rect x="2.5" y="4" width="8" height="5.5" fill="none" stroke="#d9b443"/><path d="M2.5 4l4 3 4-3" fill="none" stroke="#d9b443"/></svg>
          paul@vorasti.com
        </li>
        <li>
          <svg viewBox="0 0 13 13"><rect width="13" height="13" fill="#111"/><rect x="3" y="5" width="7" height="4.5" fill="#d9b443"/><rect x="4.5" y="2.5" width="4" height="2.5" fill="none" stroke="#d9b443"/></svg>
          555-384-1962
        </li>
      </ul>
    </div>
  </section>

</body>
</html>
```